Clearpath Ledger Billing Company Business card

Need a business card that stands out that includes name of company,(above) Owners name Marisol Whitfield phone#555-314-7762 email# ClearpathLedgerBC@mailbox-example.com and website www.Clearpathledgerbillingcompany-example.com. This is a medical billing company so the card has to relate to that or relate to steady cashflow

```html
<!DOCTYPE html>
<html lang="en">
<head>
<meta charset="utf-8">
<title>Clearpath Ledger Billing Company – Business Card</title>
<link rel="stylesheet" href="https://fonts.googleapis.com/css2?family=Open+Sans:wght@400;700&display=swap">
<style>
  :root {
    --navy: #1d4f76;
    --green: #5f9f2e;
    --ink: #333a40;
    --card: #ffffff;
    --page: #e9ebec;
    --rule: #c9cdd0;
  }
  * { box-sizing: border-box; margin: 0; padding: 0; }
  html, body {
    width: 1200px; height: 970px; overflow: hidden;
    background: var(--page);
  }
  .card {
    position: absolute; left: 100px; top: 207px;
    width: 1000px; height: 556px;
    background: var(--card);
    border: 1px solid #d4d8db;
    overflow: hidden;
    font-family: "Open Sans", Arial, sans-serif;
  }
  .brand {
    position: absolute; left: 48px; top: 130px;
    display: flex; align-items: center; gap: 20px;
  }
  .brand-dot {
    width: 64px; height: 64px; flex: none;
    border-radius: 50%; background: var(--green);
  }
  .brand-name {
    font-weight: 700; color: var(--navy);
    font-size: 34px; line-height: 1.2;
  }
  .divider {
    position: absolute; left: 48px; top: 341px; width: 612px; height: 1px;
    background: var(--rule);
  }
  .owner {
    position: absolute; left: 672px; top: 322px;
    font-weight: 700; font-size: 26px; color: var(--navy); letter-spacing: 0.3px;
    text-transform: uppercase; white-space: nowrap;
  }
  .contacts { position: absolute; left: 48px; top: 376px; list-style: none; }
  .contacts li {
    display: flex; align-items: center; gap: 12px;
    height: 36px; font-size: 22px; color: var(--ink);
  }
  .contacts svg { width: 22px; height: 22px; fill: var(--ink); flex: none; }
  .bands { position: absolute; left: 0; bottom: 0; width: 1000px; height: 60px; }
</style>
</head>
<body>
  <div class="card">
    <div class="brand">
      <span class="brand-dot"></span>
      <div class="brand-name">Clearpath Ledger<br>Billing Company</div>
    </div>

    <div class="divider"></div>
    <div class="owner">Marisol Whitfield</div>

    <ul class="contacts">
      <li>
        <svg viewBox="0 0 24 24" aria-hidden="true"><path d="M3 9c0-3 4-5 9-5s9 2 9 5v2h-5V9c-1-.6-2.5-1-4-1s-3 .4-4 1v2H3z"/><path d="M7 12h10l3 8H4z"/></svg>
        555-314-7762
      </li>
      <li>
        <svg viewBox="0 0 24 24" aria-hidden="true"><path d="M2 5h20v14H2z" /><path d="M2 5l10 8 10-8" fill="none" stroke="#fff" stroke-width="1.8"/></svg>
        ClearpathLedgerBC@mailbox-example.com
      </li>
      <li>
        <svg viewBox="0 0 24 24" aria-hidden="true"><circle cx="12" cy="12" r="10"/><path d="M2 12h20M12 2c3 3 3 17 0 20M12 2c-3 3-3 17 0 20" fill="none" stroke="#fff" stroke-width="1.4"/></svg>
        Clearpathledgerbillingcompany-example.com
      </li>
    </ul>

    <svg class="bands" viewBox="0 0 1000 60" preserveAspectRatio="none" aria-hidden="true">
      <path d="M0 46 H560 C600 46 620 24 660 22 H1000 V60 H0 Z" fill="var(--navy)"/>
      <path d="M0 32 H520 C540 32 548 36 560 42 H0 Z" fill="var(--green)"/>
      <path d="M0 42 H560 C600 42 620 22 660 18 H1000 V22 H660 C620 24 600 46 560 46 H0 Z" fill="#ffffff"/>
    </svg>
  </div>
</body>
</html>
```